Ravel Trade Parts consulting and education services needs ClipNook channel with video intro

Well, www.raveltradeparts.example we think we have a nice Logo already but need to integrate it for a pleasing, simple. classy, all business signaling ClipNook account/channel were we are going to provide free consulting on the most common problem areas of ERP integration within the ERP system it self between the different functional modules and integration between other external systems, api webservices, digital collaboration and cloud solutions. Like exchange rates, deal grove, Orvano market place. Conceptual design and strategy level discussions on design and how to execute the implementation etc. Smallest technical tricks to history of systems and future predictions trying to help business users to navigate a more and more complex back office environment. We are using our +25 years of experience making it possible for you to challenge the IT department without having to hire a big five consulting firm. We want you to arm yourself just watching our ClipNook channel!

Target Market(s)

People working in large organizations using ERP systems - business users

Industry/Entity Type

Consulting and education providing knowledge about sytesm and integration

Colors
0054AA
0677BA
7BADD7
CADEEF
E8F1F8

Requirements
Must have
• Clean look using our existing logo
Nice to have
• message that anybody watching our videos will be able to challenge the IT department and consultants
Should not have
• Any other or new logo, many colors and not only logo should also show a message

```html
<!DOCTYPE html>
<html lang="en">
<head>
<meta charset="utf-8">
<title>Ravel Trade Parts – Connected ERP for Anybody</title>
<link rel="stylesheet" href="https://fonts.googleapis.com/css2?family=Roboto:wght@700;900&display=swap">
<style>
  :root {
    --navy-deep: #141c3f;
    --navy: #222b57;
    --slate: #6b7290;
    --mist: #c9ccd8;
    --paper: #f6f7fa;
    --white: #ffffff;
    --ink: #000000;
    --brand-blue: #0a3596;
    --brand-sky: #0054aa;
    --hero-light: #3b63c4;
    --hero-mid: #26357a;
  }
  html, body {
    margin: 0;
    padding: 0;
    overflow: hidden;
  }
  body {
    width: 1200px;
    height: 675px;
    font-family: "Roboto", Arial, sans-serif;
  }
  .channel-banner {
    position: relative;
    width: 1200px;
    height: 675px;
    overflow: hidden;
    background: linear-gradient(90deg,
      var(--navy-deep) 0%,
      var(--navy) 48%,
      var(--slate) 64%,
      var(--mist) 82%,
      var(--paper) 100%);
  }
  .hero-visual {
    position: absolute;
    left: 0;
    top: 0;
    width: 690px;
    height: 675px;
    background: radial-gradient(ellipse 330px 360px at 370px 320px,
      var(--hero-light) 0%,
      var(--hero-mid) 45%,
      var(--navy-deep) 100%);
    -webkit-mask-image: linear-gradient(90deg, #000 75%, transparent 100%);
    mask-image: linear-gradient(90deg, #000 75%, transparent 100%);
  }
  .brand-plate {
    position: absolute;
    left: 711px;
    top: 16px;
    width: 489px;
    height: 156px;
    background: var(--white);
    border-radius: 24px 0 0 24px;
    box-shadow: 0 3px 8px rgba(20,28,63,0.25);
    display: flex;
    align-items: center;
    gap: 16px;
    padding-left: 44px;
    box-sizing: border-box;
  }
  .brand-dot {
    width: 56px;
    height: 56px;
    border-radius: 50%;
    background: var(--brand-sky);
    flex: none;
  }
  .brand-name {
    font-weight: 700;
    font-size: 38px;
    color: var(--brand-sky);
    white-space: nowrap;
  }
  .headline {
    position: absolute;
    right: 94px;
    top: 196px;
    margin: 0;
    text-align: right;
    font-weight: 900;
    font-size: 70px;
    line-height: 80px;
    letter-spacing: -0.5px;
    text-shadow: 2px 3px 4px rgba(0,0,0,0.25);
  }
  .headline span { display: block; }
  .headline .dark { color: var(--ink); }
  .headline .blue { color: var(--brand-blue); }
  .headline .for {
    display: inline-block;
    font-size: 38px;
    vertical-align: top;
    line-height: 46px;
    margin-right: 14px;
  }
</style>
</head>
<body>
  <main class="channel-banner">
    <div class="hero-visual" role="img" aria-label="Photo: businessman in a dark suit holding open hands beneath a glowing blue ERP hologram with icons for logistics, finance, analytics, manufacturing, shopping and people"></div>

    <div class="brand-plate">
      <span class="brand-dot" aria-hidden="true"></span>
      <span class="brand-name">Ravel Trade Parts</span>
    </div>

    <h1 class="headline">
      <span class="dark">Connected</span>
      <span class="blue">Enterprise</span>
      <span class="blue">Resource</span>
      <span class="blue">Planning</span>
      <span class="dark"><span class="for">for</span>Anybody</span>
    </h1>
  </main>
</body>
</html>
```